Card for Real Estate Developer

We need a business card design for a Real Estate Development company based in Texas. We focus on retail, apartment and residential development. Our target is predominantly investors looking to us to place their money properly to achieve a significant return. On the other side we sell our services to large retailers as their preferred developer assisting them in locating, building and leasing their real estate.

Target Market(s)

Investors

Industry/Entity Type

Real Estate Development

Contact Information for Business Card

Would like to stay within the company color scheme, while keeping the design moderately simple.

Font styles to use
Other font styles liked:
• per attached document

Requirements
Must have
• Name
• Phone
• Email
• Website
• Logo Prominently Displayed
• Stay within the colors provided in the attached document

```html
<!DOCTYPE html>
<html lang="en">
<head>
<meta charset="utf-8">
<title>Corvale Development – Business Card</title>
<link rel="stylesheet" href="https://fonts.googleapis.com/css2?family=Fira+Sans:wght@400;500&display=swap">
<style>
  :root {
    --brand-blue: #4a8fbe;
    --brand-blue-deep: #3f83b3;
    --brand-blue-light: #5a9dca;
    --ink: #3a3d40;
    --muted: #6a6e72;
    --card-white: #ffffff;
    --canvas: #efefef;
  }
  * { box-sizing: border-box; margin: 0; padding: 0; }
  html, body { width: 1200px; height: 1000px; overflow: hidden; }
  body {
    background: var(--canvas);
    font-family: "Fira Sans", Arial, sans-serif;
    color: var(--ink);
    position: relative;
  }
  .card {
    position: absolute;
    width: 560px;
    height: 320px;
    border-radius: 4px;
    overflow: hidden;
    box-shadow: 0 14px 30px rgba(0,0,0,0.14), 0 2px 6px rgba(0,0,0,0.08);
  }

  /* Front */
  .card-front { left: 60px; top: 470px; background: var(--card-white); }
  .front-rule {
    position: absolute; left: 34px; right: 34px; top: 34px;
    height: 2px; background: var(--brand-blue);
  }
  .contact-list {
    position: absolute; left: 34px; top: 56px;
    list-style: none; font-size: 14px; color: var(--muted);
  }
  .contact-list li { display: flex; align-items: center; gap: 10px; margin-bottom: 8px; }
  .contact-list svg { width: 14px; height: 14px; fill: var(--brand-blue); flex: none; }
  .identity {
    position: absolute; left: 0; right: 0; top: 120px; text-align: center;
  }
  .wordmark {
    font-size: 26px; font-weight: 400; color: var(--brand-blue);
    letter-spacing: 3px; text-transform: uppercase; line-height: 1.1;
  }
  .wordmark-sub {
    font-size: 12px; font-weight: 400; color: var(--brand-blue);
    letter-spacing: 6px; text-transform: uppercase;
  }
  .person-name {
    margin-top: 14px; font-size: 22px; font-weight: 500; color: var(--brand-blue);
  }
  .person-title { font-size: 11px; color: var(--muted); margin-top: 2px; }
  .address {
    position: absolute; right: 34px; bottom: 70px;
    font-size: 15px; line-height: 1.3; text-align: right; color: var(--ink);
  }
  .front-band {
    position: absolute; left: 0; right: 0; bottom: 0; height: 30px;
    background: var(--brand-blue);
  }

  /* Back */
  .card-back {
    left: 600px; top: 150px;
    background: linear-gradient(135deg, var(--brand-blue-light) 0%, var(--brand-blue) 55%, var(--brand-blue-deep) 100%);
  }
  .back-lockup {
    position: absolute; inset: 0;
    display: flex; align-items: center; justify-content: center; gap: 18px;
    color: #ffffff;
  }
  .back-square { width: 40px; height: 40px; background: #ffffff; flex: none; }
  .back-wordmark { text-align: left; }
  .back-wordmark .name {
    font-size: 38px; letter-spacing: 4px; text-transform: uppercase; line-height: 1.05;
  }
  .back-wordmark .sub {
    font-size: 16px; letter-spacing: 9px; text-transform: uppercase;
  }
</style>
</head>
<body>

<section class="card card-front" aria-label="Business card front">
  <div class="front-rule"></div>

  <ul class="contact-list">
    <li>
      <svg viewBox="0 0 24 24" aria-hidden="true"><path d="M6.6 10.8a15.1 15.1 0 0 0 6.6 6.6l2.2-2.2a1 1 0 0 1 1-.25 11.4 11.4 0 0 0 3.6.57 1 1 0 0 1 1 1V20a1 1 0 0 1-1 1A17 17 0 0 1 3 4a1 1 0 0 1 1-1h3.5a1 1 0 0 1 1 1c0 1.25.2 2.45.57 3.57a1 1 0 0 1-.25 1z"/></svg>
      555-014-2290
    </li>
    <li>
      <svg viewBox="0 0 24 24" aria-hidden="true"><path d="M2 5h20v14H2z M4 7v.5l8 5 8-5V7l-8 5z" fill-rule="evenodd"/></svg>
      dreyes@corvaledev.com
    </li>
    <li>
      <svg viewBox="0 0 24 24" aria-hidden="true"><path d="M12 2a10 10 0 1 0 0 20 10 10 0 0 0 0-20zm6.9 9h-3a15 15 0 0 0-1.3-5.6A8 8 0 0 1 18.9 11zM12 4c.9 1.2 1.8 3.6 1.9 7h-3.8c.1-3.4 1-5.8 1.9-7zM9.4 5.4A15 15 0 0 0 8.1 11h-3a8 8 0 0 1 4.3-5.6zM5.1 13h3a15 15 0 0 0 1.3 5.6A8 8 0 0 1 5.1 13zM12 20c-.9-1.2-1.8-3.6-1.9-7h3.8c-.1 3.4-1 5.8-1.9 7zm2.6-1.4a15 15 0 0 0 1.3-5.6h3a8 8 0 0 1-4.3 5.6z"/></svg>
      corvaledev.com
    </li>
  </ul>

  <div class="identity">
    <div class="wordmark">Corvale</div>
    <div class="wordmark-sub">Development</div>
    <div class="person-name">Daniel Reyes</div>
    <div class="person-title">Real Estate Developer</div>
  </div>

  <address class="address" style="font-style:normal">
    48 Elm Avenue,<br>
    Suite 310<br>
    Fairhill TX 75001
  </address>

  <div class="front-band"></div>
</section>

<section class="card card-back" aria-label="Business card back">
  <div class="back-lockup">
    <div class="back-square"></div>
    <div class="back-wordmark">
      <div class="name">Corvale</div>
      <div class="sub">Development</div>
    </div>
  </div>
</section>

</body>
</html>
```